Postcard design to acquire new clients for my Property Management Company

I'm looking for a postcard design that I can send to prospective clients detailing information about my company and services.
Postcard should be eye catching and contain information from www.brightkeyrentals-example.com. I've provided a few screen shots for the most important information and my logo.
Target Market(s)
Real Estate
Industry/Entity Type
Real Estate
Font styles to use
Sans Serif
Requirements
Must have
- Must be eye catching!! this will be a direct mail piece - I'd like for the card to be read and not tossed in the trash immediately.
Design que from the logo.
A place to write / print the receipts name and address.
our physical address - 2287 Marble Lane, Lubbock, TX 79555.
Should not have
- the contact information on the business card is not accurate - please use info from website.

```html
<!DOCTYPE html>
<html lang="en">
<head>
<meta charset="utf-8">
<title>BrightKey Rentals – Direct Mail Postcard</title>
<link rel="stylesheet" href="https://fonts.googleapis.com/css2?family=Montserrat:wght@500;600;700;800&family=Roboto:wght@400&display=swap">
<style>
  :root {
    --navy: #0f4c82;
    --grey-text: #9b9b9b;
    --grey-band: #a4a4a4;
    --grey-band-dark: #858585;
    --card-light: #efefef;
    --white: #ffffff;
    --stage: #767272;
    --rule: #8a8a8a;
  }
  * { box-sizing: border-box; margin: 0; padding: 0; }
  html, body { width: 960px; height: 1200px; overflow: hidden; }
  body { background: var(--stage); font-family: "Montserrat", Arial, sans-serif; position: relative; }

  .postcard { position: absolute; left: 154px; width: 647px; height: 432px; overflow: hidden; }
  .postcard--front { top: 117px; background: var(--card-light); }
  .postcard--back { top: 633px; background: var(--white); }
  .postcard__shapes { position: absolute; inset: 0; width: 647px; height: 432px; }

  /* Brand name */
  .brand { position: absolute; color: var(--navy); font-weight: 700; white-space: nowrap; }
  .brand--front { right: 39px; top: 48px; font-size: 19px; letter-spacing: 3px; text-align: right; }
  .brand--back { left: 305px; top: 56px; font-size: 14px; letter-spacing: 2px; }

  .return-address { position: absolute; left: 305px; top: 78px; font-size: 9px; font-weight: 500; letter-spacing: 0.6px; color: var(--navy); white-space: nowrap; }

  /* Front */
  .headline { position: absolute; right: 39px; top: 124px; text-align: right; font-weight: 800; line-height: 1; }
  .headline__line { display: block; }
  .headline__line--navy { color: var(--navy); }
  .headline__line--grey { color: var(--grey-text); }
  .headline__line--l1 { font-size: 37px; margin-bottom: 7px; }
  .headline__line--l2 { font-size: 28px; margin-bottom: 4px; }
  .headline__line--l3 { font-size: 46px; margin-bottom: 5px; }
  .headline__line--l4 { font-size: 30px; }

  .tagline { position: absolute; right: 43px; top: 286px; text-align: right; font-family: "Roboto", Arial, sans-serif; font-size: 11.5px; line-height: 15px; color: var(--navy); }

  .contact { position: absolute; color: var(--white); font-weight: 700; white-space: nowrap; }
  .contact--front { right: 39px; top: 350px; text-align: right; }
  .contact--front .contact__phone { font-size: 27px; line-height: 30px; }
  .contact--front .contact__web { font-size: 11px; letter-spacing: 0.2px; }
  .contact--back { left: 30px; top: 345px; }
  .contact--back .contact__phone { font-size: 30px; line-height: 32px; }
  .contact--back .contact__web { font-size: 12px; font-weight: 600; }

  /* Back */
  .services-intro { position: absolute; left: 30px; top: 30px; color: var(--white); }
  .services-intro__title { font-size: 23.5px; font-weight: 800; line-height: 23px; }
  .services-intro__text { font-size: 12.5px; font-weight: 500; line-height: 14px; margin-top: 5px; padding-left: 3px; }

  .service-list { position: absolute; left: 32px; top: 121px; list-style: none; color: var(--white); }
  .service-list__item { display: flex; align-items: center; height: 26px; font-size: 13.5px; font-weight: 500; }
  .service-list__icon { width: 22px; height: 18px; margin-right: 11px; fill: var(--white); }

  .stamp-box { position: absolute; left: 529px; top: 37px; width: 77px; height: 76px; border: 1px solid #555; }
  .address-label { position: absolute; left: 368px; top: 157px; font-size: 12px; font-weight: 800; color: #111; }
  .address-line { position: absolute; left: 367px; width: 239px; height: 1px; background: var(--rule); }
  .address-line--1 { top: 204px; }
  .address-line--2 { top: 242px; }
  .address-line--3 { top: 277px; }
  .address-line--4 { top: 315px; }
</style>
</head>
<body>

<section class="postcard postcard--front" aria-label="Postcard front">
  <svg class="postcard__shapes" viewBox="0 0 647 432">
    <defs>
      <linearGradient id="photoTone" x1="0" y1="0" x2="1" y2="1">
        <stop offset="0" stop-color="#3f5358"/>
        <stop offset="0.45" stop-color="#7f8a8a"/>
        <stop offset="0.8" stop-color="#b8a391"/>
        <stop offset="1" stop-color="#6b5747"/>
      </linearGradient>
    </defs>
    <polygon points="304,0 315,0 385,432 375,432" fill="#a9a9a9"/>
    <polygon points="0,0 304,0 375,432 0,432" fill="url(#photoTone)" role="img" aria-label="Photo of a person in a striped sweater handing over a set of house keys"/>
    <polygon points="338,341 647,341 647,403 338,403" fill="var(--navy)"/>
    <polygon points="338,403 381,403 380,416" fill="#2e6aa3"/>
  </svg>

  <div class="brand brand--front">BRIGHTKEY RENTALS</div>

  <h1 class="headline">
    <span class="headline__line headline__line--navy headline__line--l1">PROPERTY</span>
    <span class="headline__line headline__line--grey headline__line--l2">MANAGEMENT</span>
    <span class="headline__line headline__line--navy headline__line--l3">ACROSS</span>
    <span class="headline__line headline__line--grey headline__line--l4">LUBBOCK, TX</span>
  </h1>

  <p class="tagline">Maximize your financial returns<br>with support from our rental specialists</p>

  <div class="contact contact--front">
    <div class="contact__phone">(806)555-0142</div>
    <div class="contact__web">WWW.BRIGHTKEYRENTALS-EXAMPLE.COM</div>
  </div>
</section>

<section class="postcard postcard--back" aria-label="Postcard back">
  <svg class="postcard__shapes" viewBox="0 0 647 432" aria-hidden="true">
    <polygon points="0,0 225,0 343,339 0,339" fill="var(--navy)"/>
    <polygon points="0,406 375,406 385,432 0,432" fill="var(--navy)"/>
    <polygon points="369,403 402,402 375,412" fill="var(--grey-band-dark)"/>
    <polygon points="0,339 369,339 402,402 369,406 0,406" fill="var(--grey-band)"/>
  </svg>

  <div class="services-intro">
    <h2 class="services-intro__title">DISCOVER<br>OUR SERVICES</h2>
    <p class="services-intro__text">We offer full-service property<br>management solutions</p>
  </div>

  <ul class="service-list">
    <li class="service-list__item"><svg class="service-list__icon" viewBox="0 0 22 18"><path d="M11 1 1 9.5 2.5 11 4 9.8V17h5v-5h4v5h5V9.8l1.5 1.2L21 9.5 17 6V2h-3v1.5z"/></svg>Property Marketing</li>
    <li class="service-list__item"><svg class="service-list__icon" viewBox="0 0 22 18"><circle cx="7.5" cy="5" r="4"/><circle cx="16" cy="5.5" r="3.3"/><path d="M0 17c0-5 3-7.5 7.5-7.5S15 12 15 17zM16 17c0-2.5-.6-4.6-1.8-6.2 4 .2 7.8 1.5 7.8 6.2z"/></svg>Tenant Screening</li>
    <li class="service-list__item"><svg class="service-list__icon" viewBox="0 0 22 18"><path d="M10 0h2v2.2c2 .3 3.3 1.4 3.7 3.2l-2 .5c-.3-1.2-1.3-1.9-2.8-1.9-1.6 0-2.5.7-2.5 1.7 0 1 .8 1.4 2.9 1.9 2.6.6 4.5 1.5 4.5 4 0 2-1.5 3.4-3.8 3.7V18h-2v-2.7c-2.3-.3-3.8-1.6-4.1-3.6l2-.4c.3 1.4 1.5 2.2 3.1 2.2 1.8 0 2.7-.7 2.7-1.8 0-1-.8-1.5-3-2-2.6-.6-4.4-1.5-4.4-3.900-1.8 1.4-3.2 3.7-3.6z"/></svg>Rent Collection</li>
    <li class="service-list__item"><svg class="service-list__icon" viewBox="0 0 22 18"><path d="M10 2 14 0 20 6 17 9 15 7 4 18 1 15 12 4z"/></svg>Maintenance</li>
    <li class="service-list__item"><svg class="service-list__icon" viewBox="0 0 22 18"><path d="M9 0a7 7 0 0 1 5.7 11.1L19.5 16 18 17.5l-4.9-4.8A7 7 0 1 1 9 0zm0 2.3a4.7 4.7 0 1 0 0 9.4 4.7 4.7 0 0 0 0-9.4z"/></svg>Property Inspections</li>
    <li class="service-list__item"><svg class="service-list__icon" viewBox="0 0 22 18"><path d="M1 1h1.6v14.4H21V17H1zM5 8h2v6H5zm4-4h2v10H9zm4 3h2v7h-2zm4-4h2v11h-2z"/></svg>Financial Reporting</li>
    <li class="service-list__item"><svg class="service-list__icon" viewBox="0 0 22 18"><path d="M11 0l8 3v5c0 5-3.5 8.5-8 10-4.5-1.5-8-5-8-10V3zm0 2.3L5.3 4.4V8c0 3.7 2.4 6.4 5.7 7.7z"/></svg>Evictions</li>
    <li class="service-list__item"><svg class="service-list__icon" viewBox="0 0 22 18"><path d="M10 0h2v3h7v1.5h-1.3L21 11c0 2-1.5 3-3.5 3S14 13 14 11l3.3-6.5H12V16h4v2H6v-2h4V4.5H4.7L8 11c0 2-1.5 3-3.5 3S1 13 1 11l3.3-6.5H3V3h7zM4.5 6.3 2.6 10.5h3.8zm13 0-1.9 4.2h3.8z"/></svg>Legal Guidance</li>
  </ul>

  <div class="contact contact--back">
    <div class="contact__phone">(806)555-0142</div>
    <div class="contact__web">WWW.BRIGHTKEYRENTALS-EXAMPLE.COM</div>
  </div>

  <div class="brand brand--back">BRIGHTKEY RENTALS</div>
  <p class="return-address">2287 Marble Lane, Lubbock, TX 79555</p>
  <div class="stamp-box" aria-label="Stamp area"></div>

  <div class="address-label">TO</div>
  <div class="address-line address-line--1"></div>
  <div class="address-line address-line--2"></div>
  <div class="address-line address-line--3"></div>
  <div class="address-line address-line--4"></div>
</section>

</body>
</html>
```